Healthcare technology company needs website design

We need a logo for a new company based in the U.S. We develop software to assist consumers identifying lowest cost healthcare coverage methods, including insurance, discount cards, and cash options. We would like to see designs that use multiple shades of green with the optional addition of other complimentary colors. The final design should communicate a unique blend of saving money while receiving the healthcare you need.
Need the following pages/sections: Homepage, Solutions, About Us, Contact
Competitors: www.velorimed.example; www.qzplo.example

Target Market(s)

Businesses

Industry/Entity Type

Healthcare

Coding

Coded - Design and coding required

Number of Pages Required

4 page

Colors
0054AA
0677BA
7BADD7
CADEEF
E8F1F8
00AB8E
00BBA5
67D7C9
C6EFE9
E9F9F6

Requirements
Must have
• Matching color theme with logo
Nice to have
• Animated background

```html
<!DOCTYPE html>
<html lang="en">
<head>
<meta charset="utf-8">
<title>Leafpath Health – Save Money + Get Healthcare</title>
<link rel="stylesheet" href="https://fonts.googleapis.com/css2?family=Poppins:wght@300;400;500;600;700;800&display=swap">
<style>
:root{
  --green:#2aa845;
  --green-bright:#35b94f;
  --green-dark:#1d6f2f;
  --green-deep:#17612a;
  --ink:#2b2b2b;
  --body:#555;
  --rule:#7badd7;
  --soft-grey:#eceeed;
  --white:#fff;
}
*{margin:0;padding:0;box-sizing:border-box}
html,body{width:1200px;height:3502px;overflow:hidden}
body{position:relative;font-family:'Poppins',sans-serif;background:var(--white);color:var(--ink)}
.abs{position:absolute}
.btn{display:inline-flex;align-items:center;justify-content:center;height:36px;padding:0 22px;white-space:nowrap;
  background:linear-gradient(180deg,#2ea746,#1b6d2d);color:var(--white);font-size:13px;font-weight:600;
  letter-spacing:.5px;border-radius:18px 4px 18px 18px;box-shadow:0 3px 6px rgba(0,0,0,.18);text-transform:uppercase}
.btn.abs{position:absolute}
.photo{position:absolute;overflow:hidden}
/* header */
.brand{position:absolute;display:flex;align-items:center;gap:10px;font-weight:700;color:var(--green-dark);white-space:nowrap}
.brand-dot{width:34px;height:34px;border-radius:50%;background:var(--green)}
.nav{position:absolute;top:50px;font-size:14px;font-weight:500;color:#222}
.nav.active{color:var(--green)}
.demo{position:absolute;left:982px;top:41px;width:157px;height:37px;border-radius:19px;background:var(--green-bright);
  color:#fff;font-size:13px;font-weight:600;display:flex;align-items:center;justify-content:center;white-space:nowrap}
/* hero */
.hero{position:absolute;left:60px;top:218px;width:520px}
.eyebrow{font-size:22px;letter-spacing:4px;color:var(--green-dark);font-weight:400;line-height:28px}
.hero-title{font-size:56px;line-height:66px;font-weight:700;color:var(--green-dark);margin-left:-2px}
.hero-title .hi{color:var(--green-bright)}
.lead{font-size:15.5px;line-height:27px;color:#333;width:430px;margin-top:12px}
.hero .btn{margin-top:26px;padding:0 24px}
/* section titles */
.sec-title{position:absolute;left:0;width:1200px;text-align:center;font-size:38px;font-weight:600;color:var(--green)}
.sec-sub{position:absolute;left:0;width:1200px;display:flex;justify-content:center;align-items:center;gap:10px;font-size:15px;color:#555}
.sec-sub::before,.sec-sub::after{content:"";width:130px;height:1px;background:var(--rule)}
/* benefits */
.benefit{position:absolute;top:761px;width:262px;text-align:center}
.benefit-icon{width:111px;height:111px;margin:0 auto;border:3px solid var(--green-deep);border-radius:56px 56px 0 56px;
  display:flex;align-items:center;justify-content:center}
.benefit p{margin-top:27px;font-size:13.5px;line-height:22px;color:#555}
/* text blocks */
.block{position:absolute;width:545px}
.block-title{font-size:38px;font-weight:600;color:var(--green);line-height:46px;white-space:nowrap}
.block-sub{display:flex;align-items:center;gap:10px;font-size:15px;color:#555;margin-top:4px}
.block-sub::after{content:"";width:130px;height:1px;background:var(--rule)}
.copy{font-size:13.2px;line-height:22px;color:#555}
.svc-h{font-size:31px;font-weight:500;color:var(--ink);line-height:40px}
.svc-lede{font-size:17.5px;line-height:27px;color:var(--green);margin-top:16px}
.svc-body{font-size:13.2px;line-height:24.5px;color:#555;margin-top:10px}
.svc .btn{margin-top:26px;padding:0 22px}
.arch{position:absolute;width:337px;height:335px;border-radius:168px 168px 0 0;border:5px solid var(--green-deep);overflow:hidden}
/* footer */
.f-head{position:absolute;top:3267px;font-size:17px;font-weight:600;color:var(--green)}
.f-head::after{content:"";display:block;width:22px;height:2px;background:var(--green);margin-top:8px}
.f-link{position:absolute;font-size:13.5px;color:#333;line-height:22.5px;white-space:nowrap}
.social{position:absolute;top:3346px;width:30px;height:30px;border-radius:50%;background:#eaf6ec;border:1px solid #cfe8d4}
.social.first{background:var(--green)}
</style>
</head>
<body>

<!-- header -->
<div class="abs" style="left:775px;top:-40px;width:480px;height:80px;border-radius:50%;background:var(--soft-grey)"></div>
<div class="brand" style="left:60px;top:60px;font-size:17px;letter-spacing:.5px">
  <span class="brand-dot"></span>LEAFPATH HEALTH
</div>
<span class="nav active" style="left:588px">Home</span>
<span class="nav" style="left:680px">Solutions</span>
<span class="nav" style="left:795px">About Us</span>
<span class="nav" style="left:908px">Contact</span>
<span class="demo">REQUEST A DEMO</span>

<!-- hero -->
<div class="photo" role="img" aria-label="Photo of a smiling family of three looking at a laptop together at home"
  style="left:614px;top:86px;width:586px;height:514px;border-radius:230px 0 0 190px / 300px 0 0 300px;
  background:linear-gradient(135deg,#d9d4cb,#b9ad9c 45%,#7c8a80 75%,#5aa29a)"></div>
<div class="hero">
  <div class="eyebrow">WITH LEAFPATH HEALTH</div>
  <div class="hero-title"><span class="hi">Save</span> Money +<br>Get <span class="hi">Healthcare</span></div>
  <p class="lead">Lorem ipsum dolor sit amet, consectetuer adipiscing elit, sed diam nonummy nibh euismod tincidunt.</p>
  <span class="btn">Get Started</span>
</div>

<!-- benefits -->
<div class="sec-title" style="top:664px">WE HELP YOU WITH</div>
<div class="sec-sub" style="top:711px">Benefits</div>

<div class="benefit" style="left:57px">
  <div class="benefit-icon">
    <svg width="62" height="62" viewBox="0 0 62 62" fill="none" stroke="#1d6f2f" stroke-width="2.4" stroke-linecap="round" stroke-linejoin="round">
      <path d="M31 30 C20 22 17 12 24 9 C28 7 31 11 31 13 C31 11 34 7 38 9 C45 12 42 22 31 30Z"/>
      <path d="M31 13v9M26.5 17.5h9" stroke="#35b94f"/>
      <path d="M6 30 l10 12 8 4 v10 M56 30 l-10 12 -8 4 v10"/>
      <path d="M16 42 l-2-8 M46 42 l2-8"/>
    </svg>
  </div>
  <p>Lorem ipsum dolor sit amet, consectetuer adipiscing elit, sed diam nonummy nibh euismod tincidunt.</p>
</div>
<div class="benefit" style="left:331px">
  <div class="benefit-icon">
    <svg width="62" height="62" viewBox="0 0 62 62" fill="none" stroke="#1d6f2f" stroke-width="2.4" stroke-linecap="round">
      <ellipse cx="24" cy="12" rx="14" ry="4"/>
      <path d="M10 12v6c0 2 6 4 14 4s14-2 14-4v-6M10 18v7c0 2 6 4 14 4M10 25v7c0 2 6 4 14 4M10 32v7c0 2 6 4 14 4 M10 39v6c0 2 6 4 14 4"/>
      <circle cx="42" cy="40" r="13" stroke="#35b94f"/>
      <path d="M46 35c-1-2-7-2-7 1s7 2 7 5-6 3-7 1M42 31v2M42 47v2" stroke="#35b94f"/>
    </svg>
  </div>
  <p>Lorem ipsum dolor sit amet, consectetuer adipiscing elit, sed diam nonummy nibh euismod tincidunt.</p>
</div>
<div class="benefit" style="left:607px">
  <div class="benefit-icon">
    <svg width="62" height="62" viewBox="0 0 62 62" fill="none" stroke="#1d6f2f" stroke-width="2.4" stroke-linecap="round">
      <rect x="6" y="8" width="50" height="36" rx="3"/>
      <path d="M24 44l-3 10M38 44l3 10M18 54h26"/>
      <rect x="12" y="14" width="14" height="12" stroke="#35b94f"/>
      <path d="M19 17v6M16 20h6M31 16h18M31 22h18M12 32h37M12 38h25" stroke="#35b94f"/>
    </svg>
  </div>
  <p>Lorem ipsum dolor sit amet, consectetuer adipiscing elit, sed diam nonummy nibh euismod tincidunt.</p>
</div>
<div class="benefit" style="left:881px">
  <div class="benefit-icon">
    <svg width="62" height="62" viewBox="0 0 62 62" fill="none" stroke="#1d6f2f" stroke-width="2.4" stroke-linecap="round" stroke-linejoin="round">
      <rect x="10" y="8" width="36" height="48" rx="3"/>
      <rect x="20" y="4" width="16" height="8" rx="2"/>
      <path d="M18 20v6M15 23h6M26 23h13M16 32h22M16 40h14"/>
      <path d="M45 34l10 4v7c0 6-5 9-10 11-5-2-10-5-10-11v-7z" stroke="#35b94f"/>
      <path d="M40 45l4 3 6-7" stroke="#35b94f"/>
    </svg>
  </div>
  <p>Lorem ipsum dolor sit amet, consectetuer adipiscing elit, sed diam nonummy nibh euismod tincidunt.</p>
</div>

<!-- about -->
<div class="photo" role="img" aria-label="Photo of a doctor giving a high five to a young girl sitting on her mother's lap"
  style="left:0;top:1030px;width:548px;height:469px;border-radius:0 200px 0 0 / 0 260px 0 0;border-right:5px solid var(--green);
  background:linear-gradient(120deg,#8fb4c6,#c9b7a6 45%,#e7d3bc 70%,#b8a08a)"></div>
<div class="block" style="left:599px;top:1093px;width:540px">
  <div class="block-title">A NEW WAY TO HEALTHCARE</div>
  <div class="block-sub">About Us</div>
  <p class="copy" style="margin-top:18px">Lorem ipsum dolor sit amet, consectetuer adipiscing elit, sed diam nonummy nibh euismod tincidunt ut laoreet dolore magna aliquam erat volutpat. Ut wisi enim ad minim veniam, quis nostrud exerci tation ullamcorper suscipit lobortis nisl ut aliquip ex ea commodo consequat.</p>
  <p class="copy" style="margin-top:10px">Duis autem vel eum iriure dolor in hendrerit in vulputate velit esse molestie consequat, vel illum dolore eu feugiat nulla facilisis at vero eros et accumsan et iusto odio dignissim qui blandit praesent luptatum zzril delenit augue duis dolore te feugait nulla facilisi.</p>
  <span class="btn" style="margin-top:22px;padding:0 20px">Read More</span>
</div>

<!-- services -->
<div class="sec-title" style="top:1562px">SERVICES WE PROVIDE</div>
<div class="sec-sub" style="top:1611px">Solutions</div>

<div class="block svc" style="left:61px;top:1682px">
  <div class="svc-h">Insurance</div>
  <p class="svc-lede">Lorem ipsum dolor sit amet, consectetuer adipiscing elit, sed diam nonummy nibh euismod tincidunt ut laoreet dolore magna.</p>
  <p class="svc-body">Ut wisi enim ad minim veniam, quis nostrud exerci tation ullamcorper suscipit lobortis nisl ut aliquip ex ea commodo consequat. Duis autem vel eum iriure dolor in hendrerit in vulputate velit esse molestie consequat, vel illum dolore eu feugiat nulla facilisis at vero eros et accumsan et iusto odio dignissim qui blandit praesent luptatum zzril delenit augue duis dolore te feugait nulla facilisi.</p>
  <span class="btn">Get Started</span>
</div>
<div class="arch" role="img" aria-label="Photo of a desktop monitor showing a health insurance page"
  style="left:723px;top:1672px;background:linear-gradient(150deg,#e8ecef,#c9d2d8 50%,#e7d98a 85%)"></div>

<div class="arch" role="img" aria-label="Photo of a hand holding a tablet showing a discount card screen"
  style="left:140px;top:2070px;background:linear-gradient(150deg,#e4e2de,#e88a92 45%,#e7e3df 80%)"></div>
<div class="block svc" style="left:602px;top:2079px">
  <div class="svc-h">Discount Cards</div>
  <p class="svc-lede">Lorem ipsum dolor sit amet, consectetuer adipiscing elit, sed diam nonummy nibh euismod tincidunt ut laoreet dolore magna.</p>
  <p class="svc-body">Ut wisi enim ad minim veniam, quis nostrud exerci tation ullamcorper suscipit lobortis nisl ut aliquip ex ea commodo consequat. Duis autem vel eum iriure dolor in hendrerit in vulputate velit esse molestie consequat, vel illum dolore eu feugiat nulla facilisis at vero eros et accumsan et iusto odio dignissim qui blandit praesent luptatum zzril delenit augue duis dolore te feugait nulla facilisi.</p>
  <span class="btn">Get Started</span>
</div>

<div class="block svc" style="left:61px;top:2480px">
  <div class="svc-h">Cash Options</div>
  <p class="svc-lede">Lorem ipsum dolor sit amet, consectetuer adipiscing elit, sed diam nonummy nibh euismod tincidunt ut laoreet dolore magna.</p>
  <p class="svc-body">Ut wisi enim ad minim veniam, quis nostrud exerci tation ullamcorper suscipit lobortis nisl ut aliquip ex ea commodo consequat. Duis autem vel eum iriure dolor in hendrerit in vulputate velit esse molestie consequat, vel illum dolore eu feugiat nulla facilisis at vero eros et accumsan et iusto odio dignissim qui blandit praesent luptatum zzril delenit augue duis dolore te feugait nulla facilisi.</p>
  <span class="btn">Get Started</span>
</div>
<div class="arch" role="img" aria-label="Photo of a smiling man holding a fan of banknotes and pointing at them"
  style="left:723px;top:2467px;background:linear-gradient(150deg,#c9ccce,#a8abad 50%,#8a7a6b 80%)"></div>

<!-- call to action band -->
<div class="abs" style="left:0;top:2878px;width:1200px;height:330px;background:linear-gradient(90deg,#2a9a44,#34b04d 55%,#4cc061)"></div>
<div class="photo" role="img" aria-label="Photo of a happy couple sitting on a sofa looking at a laptop"
  style="left:0;top:2878px;width:430px;height:330px;border-radius:0 330px 0 0 / 0 330px 0 0;
  background:linear-gradient(120deg,#e6e2dc,#b7a79a 50%,#6d8a8f)"></div>
<div class="abs" style="left:561px;top:2962px;font-size:36px;line-height:46px;font-weight:600;color:#fff;white-space:nowrap">START BUILDING YOUR HEALTH<br>SAVINGS TODAY</div>
<span class="btn abs" style="left:562px;top:3077px;background:transparent;border:2px solid #fff;box-shadow:none">Get Started</span>

<!-- footer -->
<div class="brand" style="left:60px;top:3282px;font-size:24px;letter-spacing:.5px">
  <span class="brand-dot" style="width:44px;height:44px"></span>LEAFPATH HEALTH
</div>
<span class="social first" style="left:111px"></span>
<span class="social" style="left:149px"></span>
<span class="social" style="left:186px"></span>
<span class="social" style="left:224px"></span>

<div class="f-head" style="left:457px">COMPANY</div>
<span class="f-link" style="left:455px;top:3310px">Home<br>Solutions<br>About Us<br>Contact</span>
<div class="f-head" style="left:703px">SOLUTIONS</div>
<span class="f-link" style="left:703px;top:3310px">Insurance<br>Discount Cards<br>Cash Options</span>
<div class="f-head" style="left:954px">LEGAL</div>
<span class="f-link" style="left:952px;top:3310px">Support<br>Privacy Policy<br>Terms &amp; Conditions</span>

<div class="abs" style="left:0;top:3456px;width:1200px;height:46px;background:var(--green-bright);display:flex;align-items:center;justify-content:center;color:#fff;font-size:12px;font-weight:600">© LEAFPATH HEALTH - 2022. All Rights Reserved.</div>

</body>
</html>
```